Korven GYM

customer is looking for a quiet, but present design on his silver-colored Marlo haulette. https://korvengym-example.nl/

the design can be like half if a wrap, with a nice picture in the background and his logo on top of it

```html
<!DOCTYPE html>
<html lang="nl">
<head>
<meta charset="utf-8">
<title>Korven GYM – Marlo haulette wrap</title>
<link href="https://fonts.googleapis.com/css2?family=Bebas+Neue&family=Roboto+Slab:wght@800&family=Oswald:wght@600&display=swap" rel="stylesheet">
<style>
  :root {
    --canvas: #e6e7e9;
    --panel-black: #0d0d0d;
    --brand-blue: #1d9ad6;
    --ink: #141414;
    --white: #ffffff;
  }
  html, body { margin: 0; padding: 0; overflow: hidden; }
  body { width: 1200px; height: 1000px; background: var(--canvas); position: relative; font-family: "Bebas Neue", "Oswald", sans-serif; }

  .photo-band {
    position: absolute; left: 420px; top: 200px; width: 720px; height: 280px;
    display: flex; background: var(--panel-black);
  }
  .photo-band .photo { flex: 0 0 146px; height: 100%; }
  .photo--cardio { background: linear-gradient(160deg, #8a6a52, #3d2c22 60%, #1e1714); }
  .photo--kracht { background: linear-gradient(160deg, #6b5446, #2f2520 55%, #15110f); }
  .photo--groep { background: linear-gradient(150deg, #3c5f9c, #8b5040 55%, #2a1f1d); }
  .photo--kids { background: linear-gradient(160deg, #9b9490, #d9d5d2 50%, #4b4542); }

  .photo-band .label {
    flex: 0 0 34px; height: 100%; background: var(--panel-black);
    display: flex; align-items: flex-end; justify-content: center;
  }
  .label span {
    writing-mode: vertical-rl; transform: rotate(180deg);
    font-family: "Roboto Slab", Georgia, serif; font-weight: 800;
    font-size: 20px; color: var(--white); padding-bottom: 0; margin-bottom: auto; padding-top: 8px;
  }

  .arrow { position: absolute; left: 90px; top: 570px; width: 700px; height: 110px; }

  .slogan {
    position: absolute; left: 250px; top: 688px; margin: 0;
    font-size: 34px; color: var(--ink); letter-spacing: 0.5px;
  }
  .slogan small { font-size: 18px; }

  .contact {
    position: absolute; left: 250px; top: 750px; margin: 0;
    display: flex; align-items: center; gap: 14px;
    font-size: 36px; color: var(--ink);
  }
  .contact .dot-link {
    width: 34px; height: 34px; border-radius: 50%; background: var(--brand-blue);
  }

  .brand {
    position: absolute; left: 830px; top: 580px; width: 310px;
  }
  .brand .name-block {
    background: var(--panel-black); padding: 14px 20px 8px;
  }
  .brand .name {
    margin: 0; font-family: "Bebas Neue", sans-serif; font-size: 72px; line-height: 1;
    color: var(--white); letter-spacing: 2px;
  }
  .brand .tagline {
    margin: 8px 0 0; font-family: "Oswald", sans-serif; font-weight: 600;
    font-size: 18px; letter-spacing: 3px; color: var(--brand-blue); text-align: right;
  }
</style>
</head>
<body>

  <section class="photo-band">
    <div class="photo photo--cardio" role="img" aria-label="Illustratie van een vrouw die traint op een spinningfiets"></div>
    <div class="label"><span>Cardio</span></div>
    <div class="photo photo--kracht" role="img" aria-label="Illustratie van een man die met halters traint"></div>
    <div class="label"><span>Krachttraining</span></div>
    <div class="photo photo--groep" role="img" aria-label="Illustratie van een vrouw met bokshandschoenen in een groepsles"></div>
    <div class="label"><span>Groepslessen</span></div>
    <div class="photo photo--kids" role="img" aria-label="Illustratie van een kind in vechtsportkleding tijdens een kidsles"></div>
    <div class="label"><span>Kidslessen</span></div>
  </section>

  <svg class="arrow" viewBox="0 0 700 110" aria-hidden="true">
    <polygon points="0,55 110,10 95,48 95,62 110,100" fill="var(--brand-blue)"/>
    <rect x="95" y="48" width="540" height="14" fill="var(--brand-blue)"/>
    <polyline points="600,12 640,55 600,98" fill="none" stroke="var(--brand-blue)" stroke-width="13"/>
    <polyline points="640,12 680,55 640,98" fill="none" stroke="var(--brand-blue)" stroke-width="13"/>
  </svg>

  <p class="slogan">Do it now don't wait for tomorrow <small>(Dirk Varnel)</small></p>

  <p class="contact">
    <span>www.korvengym-example.nl • Volg ons op:</span>
    <span class="dot-link" aria-hidden="true"></span>
    <span class="dot-link" aria-hidden="true"></span>
  </p>

  <div class="brand">
    <div class="name-block"><p class="name">KORVEN GYM</p></div>
    <p class="tagline">TRAINING CENTRE</p>
  </div>

</body>
</html>
```